Process / Concept needing modern design rework

We've got a 1 page PDF flowchart graphic that forms the basis of our strategy working with clients and we need this to be redesigned in a more modern, clear and effective way. The final design should allow us to make some changes (we have some skills in adobe indesign / illustrator etc so are happy to tweak content from your design.

Our brand uses primarily oranges, greys and white. And the final flowchart should be really clear to understand for our clients. See the current PDF attached.

We are open to reimagining of the layout / design - it does not need to be laid out exactly as we have already.

EXPLAINING THE FLOWCHART:
This flowchart maps out our approach to video in a marketing strategy. Across the top is the customer journey through three phases (awareness, consideration, purchase). This then aligns with the marketing approach which is emotional on the left (at the awareness stage) through to rational to the right (at the purchase end of the journey). Under this journey flowchart we see the three main goals outlined, with the types of video that work for each goal listed under that. Then across the bottom are logos/icons indicating the video platforms that should be used for each goal.

Finally right across the bottom underlying all of this marketing strategy is the idea of video as a product. In otherwords video used not in the marketing funnel but as part of the businesses product suite or offering.

I trust that makes sense to design, feel free to play with the layout.

Target Market(s)

Corporate clients, medium enterprise

Font styles to use
Sans Serif

Colors

Designer to choose colors to be used in the design.

Requirements
Must have
• Modern, clear design. Good use of shape and colour. The three main goals for video strategy should be the key focus (left to right) Brand positioning, Social Engagement, Conversions and traffic. Must fit nicely to one a4 page, landscape is fine.

```html
<!DOCTYPE html>
<html lang="en">
<head>
<meta charset="utf-8">
<title>Customer Conversion &amp; Online Video Strategy</title>
<link href="https://fonts.googleapis.com/css2?family=Open+Sans:wght@300;400;600;700;800&display=swap" rel="stylesheet">
<style>
  :root {
    --orange: #f0821e;
    --orange-deep: #ec6a24;
    --amber: #f7b21b;
    --yellow: #fbc02d;
    --red-tag: #e8542a;
    --grey: #6d6e71;
    --white: #ffffff;
    --card-line: #f3a46b;
  }
  * { box-sizing: border-box; margin: 0; padding: 0; }
  html, body { width: 1200px; height: 800px; overflow: hidden; background: #f2f2f2; }
  body { font-family: "Open Sans", Arial, sans-serif; color: var(--grey); }
  .sheet { position: relative; width: 1200px; height: 800px; background: var(--white); overflow: hidden; }

  .brand { position: absolute; left: 60px; top: 42px; }
  .brand-row { display: flex; align-items: center; gap: 10px; }
  .brand-mark { width: 22px; height: 22px; border-radius: 50%; background: var(--orange); }
  .brand-name { font-size: 26px; font-weight: 400; color: var(--grey); letter-spacing: .2px; }
  .brand-tagline { font-size: 12px; color: var(--grey); margin: 4px 0 0 32px; }

  .title-shape { position: absolute; right: 0; top: 0; }
  .title { position: absolute; left: 690px; top: 62px; color: var(--white); }
  .title-sub { font-size: 19px; font-weight: 400; letter-spacing: 1px; }
  .title-amp { font-size: 28px; font-weight: 800; margin-left: 6px; }
  .title-main { font-size: 31px; font-weight: 800; letter-spacing: .5px; line-height: 1.15; }

  .stage { position: absolute; top: 200px; display: flex; align-items: center; gap: 8px; font-size: 20px; font-weight: 300; color: var(--grey); letter-spacing: .5px; }
  .stage-dot { width: 14px; height: 14px; background: var(--orange); border-radius: 3px; transform: rotate(45deg); }

  .approach-band { position: absolute; left: 0; top: 238px; }
  .approach { position: absolute; top: 246px; font-size: 17px; font-weight: 300; color: var(--white); }
  .tag { position: absolute; top: 282px; background: var(--red-tag); color: var(--white); font-size: 9px; font-weight: 700; letter-spacing: .8px; padding: 2px 8px; z-index: 2; }

  .card { position: absolute; top: 300px; width: 250px; height: 345px; border: 1px solid var(--card-line); border-top: none; background: var(--white); display: flex; flex-direction: column; overflow: hidden; }
  .card-head { height: 80px; flex: none; display: flex; align-items: center; justify-content: center; }
  .card-icon { position: relative; width: 62px; height: 54px; background: var(--amber); border-radius: 14px; display: flex; align-items: center; justify-content: center; }
  .card-icon::before { content: ""; position: absolute; inset: 6px -6px -6px 6px; background: var(--orange); border-radius: 14px; opacity: .55; }
  .card-icon svg { position: relative; }
  .card-goal { flex: none; height: 172px; background: var(--orange); color: var(--white); text-align: center; padding: 14px 12px 10px; display: flex; flex-direction: column; align-items: center; }
  .goal-title { font-size: 11px; font-weight: 800; letter-spacing: .6px; color: var(--grey); background: var(--white); padding: 1px 8px; margin-bottom: 7px; }
  .goal-list { list-style: none; font-size: 12px; line-height: 1.35; font-weight: 600; }
  .play { margin-top: auto; width: 24px; height: 24px; border-radius: 50%; background: var(--white); display: flex; align-items: center; justify-content: center; flex: none; }
  .play::after { content: ""; margin-left: 3px; border-left: 9px solid var(--orange-deep); border-top: 6px solid transparent; border-bottom: 6px solid transparent; }
  .card-copy { flex: 1; display: flex; align-items: center; justify-content: center; padding: 6px 16px; font-size: 9.5px; line-height: 1.4; text-align: center; color: var(--grey); }
  .platforms { flex: none; height: 32px; background: var(--orange); display: flex; align-items: center; justify-content: center; gap: 9px; }
  .platform { width: 16px; height: 16px; background: var(--white); border-radius: 3px; }

  .product-band { position: absolute; left: 60px; top: 662px; width: 794px; height: 46px; background: var(--yellow); display: flex; align-items: center; justify-content: center; gap: 12px; font-size: 18px; font-weight: 400; color: var(--orange-deep); letter-spacing: 1px; }
  .product-play { width: 30px; height: 30px; border-radius: 50%; background: var(--orange-deep); position: relative; }
  .product-play::after { content: ""; position: absolute; left: 11px; top: 8px; border-left: 11px solid var(--white); border-top: 7px solid transparent; border-bottom: 7px solid transparent; }

  .footer-shape { position: absolute; right: 0; bottom: 0; }
  .footer-note { position: absolute; right: 40px; bottom: 30px; display: flex; align-items: center; gap: 10px; color: var(--white); font-size: 11px; }
  .footer-mark { width: 24px; height: 24px; border: 2px solid var(--white); border-radius: 50%; }
</style>
</head>
<body>
<main class="sheet">

  <header class="brand">
    <div class="brand-row"><span class="brand-mark"></span><span class="brand-name">Brightpath Studio</span></div>
    <p class="brand-tagline">stories that move</p>
  </header>

  <svg class="title-shape" width="600" height="200" viewBox="0 0 600 200" aria-hidden="true">
    <polygon points="40,40 600,0 600,170 540,190 60,150" fill="#f7b21b"/>
    <polygon points="20,70 260,0 600,0 600,110 420,180 40,125" fill="#f0821e" opacity=".9"/>
    <polygon points="180,0 600,0 600,60 360,110" fill="#ec6a24" opacity=".8"/>
  </svg>
  <div class="title">
    <div class="title-sub">CUSTOMER CONVERSION<span class="title-amp">&amp;</span></div>
    <div class="title-main">ONLINE VIDEO STRATEGY</div>
  </div>

  <div class="stage" style="left:60px"><span class="stage-dot"></span>Awareness</div>
  <div class="stage" style="left:332px"><span class="stage-dot"></span>Consideration</div>
  <div class="stage" style="left:604px"><span class="stage-dot"></span>Purchase</div>
  <div class="stage" style="left:876px"><span class="stage-dot"></span>Advocate</div>

  <svg class="approach-band" width="1200" height="44" viewBox="0 0 1200 44" aria-hidden="true">
    <rect x="60" y="0" width="794" height="40" fill="#fbc02d"/>
    <polygon points="300,0 326,20 300,40 318,40 344,20 318,0" fill="#f0821e"/>
    <polygon points="572,0 598,20 572,40 590,40 616,20 590,0" fill="#f0821e"/>
    <polygon points="844,0 870,20 844,40 862,40 888,20 862,0" fill="#f0821e"/>
    <rect x="876" y="0" width="250" height="40" fill="#fbc02d"/>
  </svg>
  <span class="approach" style="left:80px">Emotional</span>
  <span class="approach" style="left:352px">Emotional/Rational</span>
  <span class="approach" style="left:624px">Rational</span>
  <span class="tag" style="left:80px">MARKETING</span>
  <span class="tag" style="left:624px">SALES</span>

  <section class="card" style="left:60px">
    <div class="card-head"><div class="card-icon"><svg width="30" height="26" viewBox="0 0 30 26"><path d="M15 25 L3 13 A7 7 0 0 1 15 4 A7 7 0 0 1 27 13 Z" fill="#fff"/></svg></div></div>
    <div class="card-goal">
      <h2 class="goal-title">BRAND POSITIONING</h2>
      <ul class="goal-list"><li>Brand Storytelling</li><li>Client Stories</li><li>Why? Videos</li><li>Video Blogging</li><li>VNR</li></ul>
      <span class="play"></span>
    </div>
    <p class="card-copy">Content designed to engage with an audience on an emotional level. Building positive brand awareness and customer buy-in through an emotive storytelling approach.</p>
    <div class="platforms"><span class="platform"></span><span class="platform"></span><span class="platform"></span><span class="platform"></span><span class="platform"></span><span class="platform"></span><span class="platform"></span></div>
  </section>

  <section class="card" style="left:332px">
    <div class="card-head"><div class="card-icon"><svg width="34" height="26" viewBox="0 0 34 26"><circle cx="17" cy="7" r="5" fill="#fff"/><circle cx="7" cy="10" r="4" fill="#fff"/><circle cx="27" cy="10" r="4" fill="#fff"/><path d="M9 24 A8 8 0 0 1 25 24 Z" fill="#fff"/><path d="M1 24 A6 6 0 0 1 11 19 L9 24Z M33 24 A6 6 0 0 0 23 19 L25 24Z" fill="#fff"/></svg></div></div>
    <div class="card-goal">
      <h2 class="goal-title">SOCIAL ENGAGEMENT</h2>
      <ul class="goal-list"><li>Video Blogging</li><li>How To / FAQs</li><li>Events</li><li>Humour / Fun</li><li>User Generated</li><li>Live Stream</li></ul>
      <span class="play"></span>
    </div>
    <p class="card-copy">Content built for social sharing. Extend your reach by engaging new prospects and existing clients with education, information and inspiration.</p>
    <div class="platforms"><span class="platform"></span><span class="platform"></span><span class="platform"></span><span class="platform"></span><span class="platform"></span><span class="platform"></span><span class="platform"></span><span class="platform"></span></div>
  </section>

  <section class="card" style="left:604px">
    <div class="card-head"><div class="card-icon"><svg width="30" height="26" viewBox="0 0 30 26"><rect x="3" y="15" width="5" height="9" fill="#fff"/><rect x="11" y="10" width="5" height="14" fill="#fff"/><rect x="19" y="6" width="5" height="18" fill="#fff"/><polyline points="2,11 10,5 16,8 27,1" fill="none" stroke="#fff" stroke-width="2"/></svg></div></div>
    <div class="card-goal">
      <h2 class="goal-title">CONVERSIONS &amp; TRAFFIC</h2>
      <ul class="goal-list"><li>Product Demos</li><li>Walk-through</li><li>Expert opinion</li><li>Service details</li><li>How To / FAQs</li><li>Landing page / Optin / CTA</li></ul>
      <span class="play"></span>
    </div>
    <p class="card-copy">Content designed to convert the engaged, qualified prospect into a buying customer. Strong sales focus with clear call to action and limited barriers to sale.</p>
    <div class="platforms"><span class="platform"></span><span class="platform"></span></div>
  </section>

  <section class="card" style="left:876px">
    <div class="card-head"><div class="card-icon"><svg width="26" height="28" viewBox="0 0 26 28"><path d="M13 1 L24 5 V13 C24 20 19 25 13 27 C7 25 2 20 2 13 V5 Z" fill="#fff"/><polyline points="8,14 12,18 19,9" fill="none" stroke="#f0821e" stroke-width="2.5"/></svg></div></div>
    <div class="card-goal" style="height:150px;padding-top:18px">
      <ul class="goal-list"><li>Engaged, current and</li><li>former customers</li><li>who love what you</li><li>do and help spread</li><li>your marketing</li></ul>
      <span class="play"></span>
    </div>
  </section>

  <div class="product-band">VIDEO AS A <span class="product-play"></span> PRODUCT</div>

  <svg class="footer-shape" width="360" height="170" viewBox="0 0 360 170" aria-hidden="true">
    <polygon points="0,170 120,40 360,0 360,170" fill="#fbc02d"/>
    <polygon points="60,170 170,30 300,60 360,120 360,170" fill="#ec6a24"/>
  </svg>
  <div class="footer-note"><span>2018 © brightpathstudio.example</span><span class="footer-mark"></span></div>

</main>
</body>
</html>
```